Whitening Pen artwork design

Whitening Pens with silkscreen printing:
sample: https://www.shopvarnel.com/Korimo-Whitening-Carbamide-Sensitivity-Travel-Friendly/dp/Q48T2K9X5R/ref=sr_1_5?dchild=1&keywords=whitening+pen&qid=1615425398&sr=8-5

inside the writing:
"teeth whitening pen " change to "FARO WHITENING PEN"
"logo" change to our logo

requirements:
Inches: 1.77" wide x 1.57" around
CM: 4.5cm wide x 4cm around

See attached file Generic Pen Artwork Placement Silkscreen – this is not a template, just a guideline, refer to the exact sizing above

- An "identifying marker" is required: Teeth Whitening Pen or Teeth Whitening Gel (for example)

-We require PDF files created to print ready specifications. Color images should be down-sampled to 300DPI

-Please provide us your Hueledger color reference for the color used in your artwork

https://www.hueledger.com/color-finder#/pick?hueBook=hueSolidCoatedV3M2

-Please ensure that all fonts are embedded in the PDF document or make sure you convert fonts to outlines to prevent any issues with fonts (AI-Type-Create Outlines)

We will need your print ready artwork in a high resolution PDF file

```html
<!DOCTYPE html>
<html lang="en">
<head>
<meta charset="utf-8">
<title>Faro Whitening Pen – Silkscreen Artwork</title>
<link rel="stylesheet" href="https://fonts.googleapis.com/css2?family=Montserrat:wght@700&family=Encode+Sans+Semi+Condensed:wght@700&family=Arimo:wght@500&display=swap">
<style>
  :root {
    --ink-slate: #424f55;
    --ink-rose: #f4b0b8;
    --ink-white: #ffffff;
    --frame-line: #9a9a9a;
    --label-ink: #1a1a1a;
  }
  * { box-sizing: border-box; margin: 0; padding: 0; }
  html, body {
    width: 1200px; height: 1200px; overflow: hidden;
    background: var(--ink-white);
  }
  .canvas { position: relative; width: 1200px; height: 1200px; }

  .print-area {
    position: absolute; left: 182px; top: 35px;
    width: 838px; height: 745px;
    border: 1px solid var(--frame-line);
    background: var(--ink-white);
  }
  .pattern-band {
    position: absolute; right: 0; top: 0;
    width: 102px; height: 100%;
    background: var(--ink-rose);
  }

  .lockup { position: absolute; left: 205px; width: 391px; }
  .lockup--top { top: 130px; }
  .lockup--bottom { top: 470px; }

  .brand { display: flex; align-items: center; height: 70px; }
  .brand__dot {
    width: 58px; height: 58px; border-radius: 50%;
    background: var(--ink-rose); flex: none;
  }
  .brand__name {
    margin-left: 22px;
    font-family: "Montserrat", sans-serif; font-weight: 700;
    font-size: 56px; line-height: 1; letter-spacing: 9px;
    color: var(--ink-slate);
    white-space: nowrap;
  }

  .product-pill {
    margin-top: 6px; height: 38px; width: 391px;
    border-radius: 19px; background: var(--ink-rose);
    display: flex; align-items: center; justify-content: center;
    overflow: hidden;
  }
  .product-pill__text {
    font-family: "Encode Sans Semi Condensed", sans-serif; font-weight: 700;
    font-size: 35px; line-height: 38px; letter-spacing: -0.6px;
    color: var(--ink-slate);
    white-space: nowrap;
  }

  .swatches { position: absolute; top: 850px; left: 0; width: 1200px; }
  .swatch { position: absolute; width: 140px; text-align: center; }
  .swatch__chip {
    width: 66px; height: 66px; margin: 0 auto;
    border: 1.5px solid #111;
  }
  .swatch__label {
    margin-top: 28px;
    font-family: "Arimo", sans-serif; font-weight: 500;
    font-size: 31px; line-height: 1; color: var(--label-ink);
    white-space: nowrap;
  }
  .swatch--slate { left: 291px; }
  .swatch--slate .swatch__chip { background: var(--ink-slate); }
  .swatch--rose { left: 532px; }
  .swatch--rose .swatch__chip { background: var(--ink-rose); }
  .swatch--white { left: 772px; }
  .swatch--white .swatch__chip { background: var(--ink-white); }
</style>
</head>
<body>
<main class="canvas">
  <section class="print-area">
    <div class="pattern-band" role="img" aria-label="Repeating brand-symbol pattern in white on rose"></div>

    <div class="lockup lockup--top">
      <div class="brand"><span class="brand__dot"></span><span class="brand__name">MERIDA</span></div>
      <div class="product-pill"><span class="product-pill__text">FARO WHITENING PEN</span></div>
    </div>

    <div class="lockup lockup--bottom">
      <div class="brand"><span class="brand__dot"></span><span class="brand__name">MERIDA</span></div>
      <div class="product-pill"><span class="product-pill__text">FARO WHITENING PEN</span></div>
    </div>
  </section>

  <section class="swatches">
    <div class="swatch swatch--slate"><div class="swatch__chip"></div><p class="swatch__label">425 C</p></div>
    <div class="swatch swatch--rose"><div class="swatch__chip"></div><p class="swatch__label">488 C</p></div>
    <div class="swatch swatch--white"><div class="swatch__chip"></div><p class="swatch__label">WHITE</p></div>
  </section>
</main>
</body>
</html>
```